Gale Sentry - WEBSITE Contest - 4-5 pages coding - Strong, simple clean WORDPRESS

Hello,
The inspiriation website is www.brixhalo.com
Please look at this site because I want to copy that.
I have changed the order a little bit so please look at my order of the site elements.
I will supply text, please just use lorem ipsum for now.
PLEASE LOOK AT THE BRIX HALO WEBSITE AND MAKE A COPY OF THAT.
PPlease look at that site and see the different features it has and make that.
We will need this main page and then:
-About Us page
-Contact Us page
-Request a quote page / fillable form
-1 product/service page
Thank you,
Trevor
/////////////////////////////
Website design for Gale Sentry.
Please design with simple, easy to read fonts. Customers are older and need strong, bold easy to read.
galesentry-demo.com
Tel (555) 318-4072
info@galesentry-demo.com
The problem is that all roofing vents leak. We have a product that goes into the vent that stops the roof from leaking.
Your beautiful Florida home is unprotected!
All roof vents leak!
Winds over 30 MPH push rainwater INTO your home through the rooftop vents! The result is water damage that can cost thousands of dollars to repair and remediate!
The GALE SENTRY is a powerful roof vent protection system, engineered to block wind driven rains from entering your home's roof vents.
The Gale Sentry is made to withstand extreme conditions. Featuring IMPACT hurricane screening and powerful steel construction.
Professional installation is permanent and concealed and is accomplished via the roof top.
Get protected for all the storms ahead! Get the Gale Sentry!
www.galesentry-demo.com
Call Now: 555 318-4072
Updates
Hello to all designers - please add a "SERVICE AREA MAP" widget to the designs. Thank you.
Target Market(s)
The target customer is a affluent, older couple 50-60 years old. Homeowner. middle class to upper class adults / ages 50-60 years old (older but not VERY old)
Industry/Entity Type
roofing and construction
Coding
Coded - Design and coding required
Number of Pages Required
4 page
Colors
Designer to choose colors to be used in the design.
Requirements
Must have
- Great landing page, about us page, product page, contact us page, request quote form / Strong, simple clean
Nice to have
- feelings: professional / strong / reliable / safety / shelter / security / future stability/ calm / security
Should not have
- stress / fear feeling - this product will remove fear and stress of damages from storms

```html
<!DOCTYPE html>
<html lang="en">
<head>
<meta charset="utf-8">
<title>Gale Sentry – Contact Us</title>
<link href="https://fonts.googleapis.com/css2?family=Montserrat:wght@300;400;500;600;700;800&family=Playfair+Display:ital@1&display=swap" rel="stylesheet">
<style>
  :root{
    --navy:#1d2b45;
    --ink:#1f2630;
    --accent:#1e7bc8;
    --teal:#2aa3c9;
    --white:#ffffff;
    --field-border:#c9d4e0;
    --muted:#8a93a0;
    --footer:#1b1c1e;
    --footer-text:#d5d7da;
  }
  *{box-sizing:border-box;margin:0;padding:0}
  html,body{width:683px;height:1200px;overflow:hidden}
  body{position:relative;font-family:"Montserrat",Arial,sans-serif;color:var(--ink);background:var(--white)}

  .site-header{position:absolute;left:0;top:0;width:683px;height:55px;background:var(--white);display:flex;align-items:center;padding:0 40px;z-index:2}
  .brand{display:flex;align-items:center;gap:8px}
  .brand-dot{width:24px;height:24px;border-radius:50%;background:var(--navy)}
  .brand-name{font-weight:800;font-size:15px;letter-spacing:.5px;color:var(--navy);line-height:1}
  .main-nav{display:flex;gap:20px;margin-left:auto;margin-right:22px}
  .main-nav a{font-size:8.5px;font-weight:500;color:var(--ink);text-decoration:none;padding-bottom:3px}
  .main-nav a.is-active{color:var(--teal);border-bottom:1.5px solid var(--teal)}
  .header-phone{display:flex;align-items:center;gap:6px;font-weight:700;font-size:10.5px;color:var(--navy)}

  .page-hero{position:absolute;left:0;top:55px;width:683px;height:132px;background:linear-gradient(180deg,#7d8a95 0%,#6f7f79 55%,#54604f 100%)}
  .page-hero::after{content:"";position:absolute;inset:0;background:rgba(25,35,55,.35)}
  .page-hero h1{position:absolute;left:0;right:0;top:66px;text-align:center;color:var(--white);font-size:27px;font-weight:300;letter-spacing:2px;z-index:1}
  .page-hero h1 b{font-weight:600}

  .quote-section{position:absolute;left:0;top:187px;width:683px;height:747px;background:linear-gradient(180deg,#283753 0%,#3f5f8c 30%,#6ea3d6 70%,#9ccdf3 100%)}
  .quote-title{position:absolute;left:0;right:0;top:93px;text-align:center;color:var(--white);font-weight:700;font-size:17px}
  .quote-title em{font-family:"Playfair Display",Georgia,serif;font-weight:400;font-size:20px}

  .field{position:absolute}
  .field label,.field .label{display:block;color:var(--white);font-size:8.5px;font-weight:500;margin-bottom:5px}
  .input{height:23px;background:var(--white);border:1px solid var(--field-border);border-radius:2px;font-size:7px;color:var(--muted);padding:0 8px;display:flex;align-items:center}
  .select{justify-content:space-between}
  .select::after{content:"";border:3px solid transparent;border-top:4px solid #555;margin-top:4px}
  .col-l{left:137px;width:200px}
  .col-r{left:346px;width:194px}
  .col-full{left:137px;width:403px}
  .textarea{height:91px;align-items:flex-start;padding-top:8px}
  .radios{display:flex;gap:22px;margin-top:14px}
  .radio{display:flex;align-items:center;gap:5px;font-size:7.5px;color:var(--white)}
  .radio i{width:8px;height:8px;border-radius:50%;border:1px solid var(--white);display:flex;align-items:center;justify-content:center}
  .radio i.on::after{content:"";width:4px;height:4px;border-radius:50%;background:var(--white)}

  .submit{position:absolute;left:251px;top:615px;width:163px;height:23px;background:var(--accent);color:var(--white);font-size:7.5px;font-weight:700;letter-spacing:.5px;display:flex;align-items:center;justify-content:center;border-radius:1px}
  .call-line{position:absolute;left:0;right:0;top:673px;text-align:center;color:var(--white);font-size:17px;font-weight:400}
  .call-line b{font-weight:700}

  .site-footer{position:absolute;left:0;top:934px;width:683px;height:266px;background:linear-gradient(180deg,#2a2c2f 0%,var(--footer) 100%);color:var(--footer-text)}
  .footer-col h3{font-size:10.5px;font-weight:700;color:var(--white);margin-bottom:12px}
  .footer-contact{position:absolute;left:91px;top:44px}
  .footer-contact li{list-style:none;display:flex;align-items:flex-start;gap:8px;font-size:7.5px;margin-bottom:9px;line-height:1.4}
  .footer-contact li span.ic{width:9px;height:9px;border-radius:50%;background:var(--footer-text);flex:none;margin-top:1px}
  .footer-brand{position:absolute;left:0;right:0;top:36px;display:flex;flex-direction:column;align-items:center;gap:10px}
  .footer-brand .brand-dot{width:44px;height:44px;background:none;border:3px solid var(--white)}
  .footer-brand .brand-name{color:var(--white);font-size:19px}
  .footer-company{position:absolute;left:497px;top:44px}
  .footer-company a{display:block;font-size:7.5px;color:var(--footer-text);text-decoration:none;margin-bottom:8px}
  .footer-bottom{position:absolute;left:40px;right:60px;top:216px;border-top:1px solid #3a3c40;padding-top:14px;display:flex;justify-content:space-between;align-items:center}
  .footer-bottom p{font-size:6.5px}
  .social{display:flex;gap:5px}
  .social span{width:12px;height:12px;border-radius:50%;background:var(--white)}
</style>
</head>
<body>

<header class="site-header">
  <div class="brand"><span class="brand-dot"></span><span class="brand-name">GALE SENTRY</span></div>
  <nav class="main-nav">
    <a href="#">About Us</a>
    <a href="#">Products</a>
    <a href="#">Service Areas</a>
    <a href="#">Blogs</a>
    <a href="#" class="is-active">Contact Us</a>
  </nav>
  <div class="header-phone">
    <svg width="10" height="10" viewBox="0 0 24 24"><path fill="#1d2b45" d="M6.6 10.8a15 15 0 0 0 6.6 6.6l2.2-2.2c.3-.3.7-.4 1-.2 1.1.4 2.3.6 3.6.6.6 0 1 .4 1 1V20c0 .6-.4 1-1 1A17 17 0 0 1 3 4c0-.6.4-1 1-1h3.5c.6 0 1 .4 1 1 0 1.3.2 2.5.6 3.6.1.3 0 .7-.2 1z"/></svg>
    555 318-4072
  </div>
</header>

<section class="page-hero" role="img" aria-label="Photo of a residential street with Florida homes and tiled roofs">
  <h1>CONTACT <b>US</b></h1>
</section>

<section class="quote-section">
  <h2 class="quote-title">Contact Us for a <em>free</em>, no obligation <em>quote</em>.</h2>

  <div class="field col-l" style="top:148px"><label>Your Name*</label><div class="input">First Name</div></div>
  <div class="field col-r" style="top:148px"><label>Your Name*</label><div class="input">Last Name</div></div>

  <div class="field col-l" style="top:200px"><label>Contact Phone*</label><div class="input">Your Phone number</div></div>
  <div class="field col-r" style="top:200px"><label>Your Email*</label><div class="input">Your Email</div></div>

  <div class="field col-l" style="top:253px"><label>Project Location*</label><div class="input">Street Address</div></div>
  <div class="field col-r" style="top:253px"><label>City*</label><div class="input">City</div></div>

  <div class="field col-l" style="top:305px"><label>State*</label><div class="input">State</div></div>
  <div class="field col-r" style="top:305px"><label>Zip Code*</label><div class="input">Zip Code</div></div>

  <div class="field col-l" style="top:360px"><span class="label">Project Type</span>
    <div class="radios"><span class="radio"><i class="on"></i>Residential</span><span class="radio"><i></i>Commercial</span></div>
  </div>
  <div class="field col-r" style="top:372px"><label>How did you hear about us?</label><div class="input select">Select</div></div>

  <div class="field col-full" style="top:428px"><label>Nature of Inquiry</label><div class="input select">Select</div></div>

  <div class="field col-full" style="top:489px"><label>Leave message (optional)</label><div class="input textarea">Message</div></div>

  <div class="submit">HAVE SOMEONE CONTACT ME</div>

  <p class="call-line">or Simply call us at <b>555 318-4072</b></p>
</section>

<footer class="site-footer">
  <div class="footer-col footer-contact">
    <h3>Contact Us</h3>
    <ul>
      <li><span class="ic"></span>Call Now: 555 318-4072</li>
      <li><span class="ic"></span>info@galesentry-demo.com</li>
      <li><span class="ic"></span>www.galesentry-demo.com</li>
      <li><span class="ic"></span>2480 Harbor Lane<br>Bayview, FL 34000</li>
    </ul>
  </div>
  <div class="footer-brand"><span class="brand-dot"></span><span class="brand-name">GALE SENTRY</span></div>
  <div class="footer-col footer-company">
    <h3>Company</h3>
    <a href="#">Home</a>
    <a href="#">About Us</a>
    <a href="#">Products</a>
    <a href="#">Contact Us</a>
  </div>
  <div class="footer-bottom">
    <p>Copyright © 2023 Gale Sentry. All Rights Reserved</p>
    <div class="social"><span></span><span></span><span></span><span></span></div>
  </div>
</footer>

</body>
</html>
```